Cover for Where the Quiet River Bends Beyond Our Morning

Cover for a book that describes everything that happens to a person, from pre-birth life plans through growing in compassion and wisdom to death and living in the afterlife. The information is revealed in messages from people living in the life after this life. The title is Lanterns Along the Hidden Stair of Every Soul: Gathered from Voices Dwelling in the Further Meadow. Author is T. Morven Ashdale. Book size is 6 by 9.

Target Market(s)

General

Font styles to use
Serif

```html
<!DOCTYPE html>
<html lang="en">
<head>
<meta charset="utf-8">
<title>Lanterns Along the Hidden Stair of Every Soul — Cover</title>
<link rel="stylesheet" href="https://fonts.googleapis.com/css2?family=Marcellus&family=Cinzel:wght@400&family=Allura&display=swap">
<style>
  :root {
    --backdrop: #d4d4d4;
    --cover-black: #141414;
    --cover-black-soft: #1d1d1d;
    --sky-top: #f6f6f6;
    --sky-mid: #dcdcdc;
    --sky-low: #b9b9b9;
    --ground: #0f0f0f;
    --title-ink: #f2f2f2;
    --subtitle-ink: #e4e4e4;
    --rule-ink: #8a8a8a;
    --author-ink: #6f6f6f;
  }
  * { margin: 0; padding: 0; box-sizing: border-box; }
  html, body {
    width: 1200px;
    height: 900px;
    overflow: hidden;
    background: var(--backdrop);
  }
  .canvas {
    position: relative;
    width: 1200px;
    height: 900px;
    display: flex;
    align-items: center;
    justify-content: center;
  }
  .book-cover {
    position: relative;
    width: 574px;
    height: 860px;
    background: radial-gradient(ellipse at 50% 60%, var(--cover-black-soft), var(--cover-black) 75%);
    overflow: hidden;
    text-align: center;
  }
  .cover-artwork {
    position: absolute;
    top: 0;
    left: 0;
    width: 100%;
    height: 357px;
    background: linear-gradient(180deg, var(--sky-top) 0%, var(--sky-mid) 45%, var(--sky-low) 82%, var(--ground) 100%);
  }
  .cover-text {
    position: absolute;
    top: 428px;
    left: 0;
    width: 100%;
    padding: 0 30px;
  }
  .title {
    font-family: "Marcellus", serif;
    font-weight: 400;
    color: var(--title-ink);
    font-size: 44px;
    line-height: 1.1;
    letter-spacing: 1px;
    text-transform: uppercase;
  }
  .title-rule {
    width: 400px;
    height: 1px;
    margin: 18px auto 14px;
    background: var(--rule-ink);
  }
  .subtitle {
    font-family: "Cinzel", serif;
    color: var(--subtitle-ink);
    font-size: 18px;
    letter-spacing: 3px;
    text-transform: uppercase;
  }
  .attribution {
    margin-top: 50px;
    font-family: "Cinzel", serif;
    color: var(--subtitle-ink);
    font-size: 11.5px;
    letter-spacing: 1.6px;
    line-height: 1.9;
    text-transform: uppercase;
  }
  .author {
    position: absolute;
    top: 735px;
    left: 0;
    width: 100%;
    font-family: "Allura", cursive;
    font-size: 30px;
    color: var(--author-ink);
  }
</style>
</head>
<body>
  <main class="canvas">
    <article class="book-cover">
      <div class="cover-artwork" role="img" aria-label="Silhouettes of one person through life, from crawling baby to child, lovers, parent lifting a baby and elderly man with a cane, walking before misty mountains with birds in the sky"></div>
      <div class="cover-text">
        <h1 class="title">Lanterns Along<br>the Hidden Stair</h1>
        <div class="title-rule"></div>
        <p class="subtitle">Of Every Soul</p>
        <p class="attribution">Gathered from<br>Voices Dwelling in the Further Meadow</p>
      </div>
      <p class="author">T. Morven Ashdale</p>
    </article>
  </main>
</body>
</html>
```